Photographic Tutorial website

We are looking for a fresh design for a photographic tutorial / workshop website. The website will have the included functions:

* Home (needs to have a login section)
* About Us
* Info about each course / workshop.
* Subscribe to courses and pay online.
* Members Area
* Photo gallery
* Contact us

The website will be implemented with our own made cms. We do not need it to be coded. We have a team ready to do this for us. We only need the PSD layout.

We have attached a mockup design that the client and I have come up with and we need the design to be taken to the next level.

Client also likes:
http://www.vellowindstudio.example/

Photographic Interests

Online

Requirements
Must have
• Must Stand out i.e black backgrounds
Should not have
• Alter the logo in anyway.

```html
<!DOCTYPE html>
<html lang="en">
<head>
<meta charset="utf-8">
<title>Lumen Trail Tuition</title>
<link rel="stylesheet" href="https://fonts.googleapis.com/css2?family=Dosis:wght@400;500;600&family=Open+Sans:ital,wght@0,400;1,400&display=swap">
<style>
:root{
  --page:#0a0a0a;
  --header:#1b1b1b;
  --nav:#222;
  --band:#1a1a1a;
  --line:#3a3a3a;
  --text:#e6e6e6;
  --muted:#bdbdbd;
  --dim:#8a8a8a;
  --bubble:#2a2a2a;
  --accent:#c9302c;
}
*{margin:0;padding:0;box-sizing:border-box}
html,body{width:904px;height:1200px;overflow:hidden;background:var(--page)}
body{position:relative;font-family:"Open Sans",sans-serif;color:var(--text)}
.abs{position:absolute}
.header{left:0;top:0;width:904px;height:113px;background:radial-gradient(ellipse at 50% 100%,#2c2c2c,#121212 70%);border-top:5px solid #333}
.brand{left:31px;top:44px;display:flex;align-items:center;gap:8px;font-family:"Dosis",sans-serif;font-weight:600;font-size:26px;color:#fff}
.brand-dot{width:22px;height:22px;border-radius:50%;background:var(--accent)}
.search{left:665px;top:50px;width:209px;height:26px;border:1px solid #444;border-radius:4px;background:#151515;font-size:9px;font-style:italic;color:#888;padding:7px 11px}
.search svg{position:absolute;right:7px;top:6px}
.nav{left:0;top:113px;width:904px;height:55px;background:linear-gradient(#262626,#1c1c1c);border-top:1px solid #333;border-bottom:1px solid #333}
.nav a{position:absolute;top:17px;font-family:"Dosis",sans-serif;font-size:14.5px;color:#e8e8e8;text-decoration:none}
.nav i{position:absolute;top:0;width:1px;height:55px;background:#3a3a3a}
.band{left:0;top:168px;width:904px;height:534px;background:linear-gradient(#161616,#262626)}
.hero{left:24px;top:169px;width:856px;height:295px;background:linear-gradient(#9fc7ea 0%,#cfe0ea 25%,#7f8a6a 45%,#4d7a2f 75%,#2e5a1c 100%)}
.hero-bar{left:24px;top:464px;width:856px;height:35px;background:#000}
.dots{left:409px;top:480px;display:flex;gap:4px}
.dots span{width:10px;height:10px;border-radius:50%;background:#fff}
.thumb{top:511px;height:175px;background:#000}
.thumb .pic{width:100%;height:147px}
.thumb p{font-family:"Dosis",sans-serif;font-size:13px;color:#eee;padding:6px 10px}
.col-h{font-family:"Dosis",sans-serif;font-size:16.5px;font-weight:500;color:#fff}
.body-t{font-size:9.6px;line-height:13.5px;color:var(--text)}
.sub-h{font-size:11px;color:#eee}
.rule{height:1px;background:var(--line)}
.vline{width:1px;background:#2a2a2a}
.row{font-size:10px;color:#ddd}
.check{font-size:10px;color:#ddd}
.blog-img{width:58px;height:50px;border:1px solid #444}
.blog-title{font-size:12.5px;color:#fff}
.bubble{left:611px;top:755px;width:261px;height:106px;background:var(--bubble);border-radius:8px;padding:9px 17px;font-size:9.6px;font-style:italic;line-height:15px;color:#aaa}
.bubble-tail{left:628px;top:860px}
.g{width:63px;height:45px}
.more{font-size:11px;color:#fff}
.footer{left:0;top:1106px;width:904px;height:94px;background:#141414;border-top:1px solid #262626}
.flinks{left:23px;top:1123px;font-size:10.5px;color:#eee;display:flex;gap:7px}
.flinks span.sep{color:#888}
.copy{left:23px;top:1152px;font-size:9.5px;color:var(--dim)}
.social{width:20px;height:20px;border-radius:50%;background:#eee;top:1120px}
</style>
</head>
<body>
<header class="abs header"></header>
<div class="abs brand"><span class="brand-dot"></span>Lumen Trail Tuition</div>
<div class="abs search">type your word
  <svg width="14" height="14" viewBox="0 0 14 14"><circle cx="6" cy="6" r="4.3" fill="none" stroke="#aaa" stroke-width="1.6"/><line x1="9.2" y1="9.2" x2="13" y2="13" stroke="#aaa" stroke-width="1.8"/></svg>
</div>

<nav class="abs nav">
  <a style="left:45px">Home</a><i style="left:94px"></i>
  <a style="left:117px">About Us</a><i style="left:187px"></i>
  <a style="left:207px">Course info</a><i style="left:288px"></i>
  <a style="left:310px">Subscribe to courses</a><i style="left:439px"></i>
  <a style="left:461px">Members Area</a><i style="left:562px"></i>
  <a style="left:582px">Photo gallery</a><i style="left:670px"></i>
  <a style="left:698px">Contact us</a>
</nav>

<div class="abs band"></div>
<div class="abs hero" role="img" aria-label="Slideshow photo of green alpine mountains with snow patches under a blue sky"></div>
<div class="abs hero-bar"></div>
<div class="abs dots"><span></span><span></span><span></span><span></span><span></span><span></span></div>

<div class="abs thumb" style="left:27px;width:147px"><div class="pic" role="img" aria-label="Black and white portrait photo" style="background:linear-gradient(#6a6a6a,#2a2a2a)"></div><p>Photo Tittle</p></div>
<div class="abs thumb" style="left:186px;width:147px"><div class="pic" role="img" aria-label="Close-up photo of meadow plants" style="background:linear-gradient(135deg,#3f6a1e,#9fbf5a 50%,#2d4a14)"></div><p>Photo Tittle</p></div>
<div class="abs thumb" style="left:345px;width:234px"><div class="pic" role="img" aria-label="Photo of a blue mountain lake" style="background:linear-gradient(#2d6fd0 0%,#8aa0b4 40%,#1e88c8 65%,#4b8a2a 100%)"></div><p>Photo Tittle</p></div>
<div class="abs thumb" style="left:587px;width:141px"><div class="pic" role="img" aria-label="Photo of palm trees at an orange sunset" style="background:linear-gradient(#c96a10,#f0a030 55%,#7a3a05)"></div><p>Photo Tittle</p></div>
<div class="abs thumb" style="left:737px;width:142px"><div class="pic" role="img" aria-label="Photo of a black car in front of a garage" style="background:linear-gradient(#8a7a6a,#c8c4c0 55%,#2a2a2a 80%,#d0d0d0)"></div><p>Photo Tittle</p></div>

<!-- Daily shooting times -->
<h2 class="abs col-h" style="left:31px;top:720px">Daily Shooting Times</h2>
<p class="abs body-t" style="left:30px;top:751px;width:236px">Brightloom Studio provides you a quality web hosting solutions. As a hosting Company we offer complete and comprehensive solutions for the web hosting.</p>
<p class="abs sub-h" style="left:28px;top:823px">Shooting Timing:-</p>
<div class="abs rule" style="left:28px;top:840px;width:228px"></div>
<div class="abs row" style="left:28px;top:848px;width:230px;line-height:17px">
  <div style="display:grid;grid-template-columns:96px 63px 60px">
    <span>Monday</span><span>08:30 AM</span><span>06:00 PM</span>
    <span>Tuesday</span><span>09:30 AM</span><span>06:00 PM</span>
    <span>Wednesday</span><span>08:30 AM</span><span>05:00 PM</span>
    <span>Friday</span><span>09:00 AM</span><span>07:00 PM</span>
    <span>Saturday</span><span>08:30 AM</span><span>07:00 PM</span>
  </div>
</div>
<p class="abs sub-h" style="left:28px;top:954px">Photographers check lists:-</p>
<div class="abs rule" style="left:28px;top:972px;width:228px"></div>
<ul class="abs check" style="left:31px;top:979px;list-style:none;line-height:17px">
  <li>›&nbsp; Wedding Shooat Checklist</li>
  <li>›&nbsp; Pre Shoot Checklist</li>
  <li>›&nbsp; Standard Checklist</li>
</ul>

<div class="abs vline" style="left:290px;top:722px;height:358px"></div>
<div class="abs vline" style="left:592px;top:722px;height:358px"></div>

<!-- Blog -->
<h2 class="abs col-h" style="left:311px;top:720px">Photography Blog</h2>
<div class="abs blog-img" role="img" aria-label="Blog thumbnail photo of a smiling man" style="left:311px;top:758px;background:linear-gradient(#e7e7e7,#8a5a3a)"></div>
<p class="abs blog-title" style="left:381px;top:753px">Tittle goes here</p>
<p class="abs body-t" style="left:381px;top:771px;width:200px">We can assure you that this is the best place for requirement of yours regarding website design solutions</p>
<div class="abs blog-img" role="img" aria-label="Blog thumbnail photo of a hand holding a camera" style="left:311px;top:841px;background:linear-gradient(#4a70b0,#b8c8e0)"></div>
<p class="abs blog-title" style="left:382px;top:837px">Tittle goes here</p>
<p class="abs body-t" style="left:382px;top:855px;width:200px">Brightloom Studio is a professional website design company dedicated to provide excellent services. We at Brightloom Studio think graphic design as a combi-nation and collaboration of ideas and tech-nology.</p>
<div class="abs blog-img" role="img" aria-label="Blog thumbnail photo of a black and white dog" style="left:312px;top:960px;background:linear-gradient(#111,#aaa)"></div>
<p class="abs blog-title" style="left:383px;top:955px">Tittle goes here</p>
<p class="abs body-t" style="left:383px;top:973px;width:200px">None of the other companies has the result we do. So stick to the best that's how you will be the best don't opt for the second best.</p>
<p class="abs more" style="left:514px;top:1049px">read more ›</p>

<!-- Testimonials -->
<h2 class="abs col-h" style="left:616px;top:720px">Testimonials</h2>
<div class="abs bubble">Brightloom Studio provides you the Search Engine Optimization making your website search engine friendly. So that the website can achieve top position and ranking in the Internet searches and thereby increasing the scope for the website to be found by customers.</div>
<svg class="abs bubble-tail" width="14" height="12" viewBox="0 0 14 12"><polygon points="0,0 14,0 4,12" fill="#2a2a2a"/></svg>
<p class="abs" style="left:641px;top:867px;font-size:11.5px;color:#fff">By Author Name</p>

<h2 class="abs col-h" style="left:616px;top:912px">Member Gallery</h2>
<div class="abs g" role="img" aria-label="Member photo of a yellow toy duck" style="left:617px;top:939px;background:linear-gradient(#6aa8e8,#e8b820)"></div>
<div class="abs g" role="img" aria-label="Member photo of a baby" style="left:684px;top:939px;background:linear-gradient(#d8c8c0,#c09070)"></div>
<div class="abs g" role="img" aria-label="Member black and white portrait" style="left:751px;top:939px;background:linear-gradient(#777,#222)"></div>
<div class="abs g" role="img" aria-label="Member photo of a child on grass" style="left:818px;top:939px;background:linear-gradient(#f4eee0,#d8b890 60%,#3a9a3a)"></div>
<div class="abs g" role="img" aria-label="Member photo of a red parrot" style="left:617px;top:994px;background:linear-gradient(135deg,#c01818,#2a70c8)"></div>
<div class="abs g" role="img" aria-label="Member black and white portrait" style="left:684px;top:994px;background:linear-gradient(#999,#333)"></div>
<div class="abs g" role="img" aria-label="Member photo of yellow orchids" style="left:751px;top:994px;background:linear-gradient(135deg,#3a2008,#e8c040,#5a3010)"></div>
<div class="abs g" role="img" aria-label="Member photo of an athlete jumping" style="left:818px;top:994px;background:linear-gradient(#3a78c8,#8ab0e0)"></div>
<p class="abs more" style="left:805px;top:1058px">view more ›</p>

<footer class="abs footer"></footer>
<div class="abs flinks"><span>Home</span><span class="sep">|</span><span>About Us</span><span class="sep">|</span><span>Course info</span><span class="sep">|</span><span>Subscribe to courses</span><span class="sep">|</span><span>Members Area</span><span class="sep">|</span><span>Photo gallery</span><span class="sep">|</span><span>Contact us</span></div>
<p class="abs copy">© 2012 Company Name &nbsp;|&nbsp; All right reserved</p>
<span class="abs social" style="left:807px"></span>
<span class="abs social" style="left:830px"></span>
<span class="abs social" style="left:853px"></span>
</body>
</html>
```